Moravel IT Customer Focused Solutions 1 Page Overview

We are looking to create a 1-page overview of our customer's IT challenges, how we assist them in resolving them, and allow their business to grow. Moravel IT, helps our customers secure their systems, minimize downtime, and allow them to focus on engaging their customer base instead of focusing on IT issues. The final design should communicate that we are safe pair of hands to manage their IT which allows them to focus on their business.

Target Market(s)

Small to Mid Size Business Owners

Industry/Entity Type

It Company

Font styles to use
Sans Serif

Requirements
Must have
• Company Logo, colour scheme that matches our logo colour, mixed with easy to read items

```html
<!DOCTYPE html>
<html lang="en">
<head>
<meta charset="utf-8">
<title>Moravel IT – Customer Focused Solutions</title>
<link rel="stylesheet" href="https://fonts.googleapis.com/css2?family=Arimo:wght@400;700&family=Josefin+Sans:wght@400;600&display=swap">
<style>
  :root {
    --gold: #d6b21c;
    --gold-deep: #c79f0f;
    --gold-light: #e4c63a;
    --ink: #222222;
    --text-grey: #555555;
    --card-bg: #eef3f7;
    --white: #ffffff;
  }
  * { box-sizing: border-box; margin: 0; padding: 0; }
  html, body { width: 1200px; height: 3492px; overflow: hidden; background: var(--white); }
  body { position: relative; font-family: "Arimo", Arial, sans-serif; color: var(--ink); }
  .heading { font-family: "Josefin Sans", "Arimo", sans-serif; font-weight: 600; letter-spacing: 2px; }

  .brand-bar { position: absolute; top: 0; left: 0; width: 1200px; height: 180px; display: flex; align-items: center; justify-content: center; }
  .brand-name { font-size: 54px; font-weight: 700; color: var(--ink); }

  .hero { position: absolute; top: 180px; left: 0; width: 1200px; height: 740px; background: radial-gradient(ellipse at 45% 40%, #5b6168 0%, #2e3237 45%, #121417 100%); }
  .hero-title { position: absolute; left: 0; right: 0; top: 520px; text-align: center; color: var(--white); font-size: 150px; font-weight: 700; line-height: 1; }

  .welcome { position: absolute; top: 920px; left: 0; width: 1200px; height: 480px; background: linear-gradient(180deg, var(--gold-light) 0%, var(--gold) 60%, var(--gold-deep) 100%); }
  .welcome-mark { position: absolute; left: 96px; top: 80px; width: 320px; height: 320px; border-radius: 50%; background: radial-gradient(circle, rgba(255,255,255,0.75) 0%, rgba(255,255,255,0.35) 60%, rgba(255,255,255,0) 72%); }
  .welcome-rule { position: absolute; left: 486px; top: 96px; width: 3px; height: 290px; background: var(--white); }
  .welcome-title { position: absolute; left: 532px; top: 112px; color: var(--white); font-size: 46px; }
  .welcome-copy { position: absolute; left: 532px; top: 200px; width: 600px; color: var(--white); font-size: 22px; line-height: 40px; }

  .section-title { position: absolute; left: 0; right: 0; text-align: center; font-size: 52px; color: var(--ink); }
  .title-rule { position: absolute; left: 570px; width: 60px; height: 4px; background: var(--gold); }

  .service { position: absolute; top: 1600px; width: 376px; height: 420px; background: var(--card-bg); padding: 28px 40px 0 16px; }
  .service svg { display: block; margin-left: 20px; }
  .service-name { margin-top: 32px; font-size: 23px; font-weight: 700; color: var(--ink); white-space: nowrap; }
  .service-rule { width: 70px; height: 3px; background: var(--gold); margin: 14px 0 26px; }
  .service-copy { font-size: 22px; line-height: 42px; color: var(--text-grey); }

  .promise { position: absolute; top: 2064px; left: 16px; width: 1168px; height: 480px; background: linear-gradient(90deg, #2a2e33 0%, #3d4249 45%, #1c1f23 75%, #0e0f11 100%); }
  .promise-line { position: absolute; left: 52px; color: var(--white); font-size: 40px; font-weight: 400; letter-spacing: 1px; }
  .promise-line .accent { color: var(--gold); }
  .promise-button { position: absolute; left: 52px; top: 288px; width: 220px; height: 64px; background: var(--gold); color: var(--white); font-size: 18px; font-weight: 700; display: flex; align-items: center; justify-content: center; letter-spacing: 1px; }

  .turbo-copy { position: absolute; top: 2756px; left: 100px; width: 1000px; text-align: center; font-size: 24px; line-height: 56px; color: var(--ink); }
  .turbo-art { position: absolute; left: 40px; top: 2910px; width: 540px; height: 410px; background: radial-gradient(ellipse at 55% 45%, #fbeeb0 0%, #f5f2e8 45%, #ffffff 80%); }
  .benefits { position: absolute; left: 640px; top: 2936px; list-style: none; }
  .benefits li { display: flex; align-items: center; gap: 26px; height: 77px; font-size: 27px; font-weight: 700; color: var(--ink); white-space: nowrap; }

  .footer { position: absolute; top: 3372px; left: 0; width: 1200px; height: 120px; background: linear-gradient(180deg, var(--gold-light), var(--gold-deep)); display: flex; align-items: center; justify-content: center; color: var(--white); font-size: 26px; }
</style>
</head>
<body>

<header class="brand-bar">
  <span class="brand-name">Moravel IT</span>
</header>

<section class="hero" role="img" aria-label="Dark photograph of a hand holding glowing gear shapes">
  <div class="hero-title">Moravel IT</div>
</section>

<section class="welcome">
  <div class="welcome-mark" role="img" aria-label="Spiral of white dots decoration"></div>
  <div class="welcome-rule"></div>
  <h2 class="welcome-title heading">WELCOME</h2>
  <p class="welcome-copy">Constant innovation around our IT services allows us to do what most IT companies only claim, which is to help you simplify, save money and deliver value to your IT companies only claim customer.</p>
</section>

<h2 class="section-title heading" style="top:1480px;">OUR SERVICES</h2>
<div class="title-rule" style="top:1554px;"></div>

<article class="service" style="left:20px;">
  <svg width="112" height="112" viewBox="0 0 112 112" fill="none" stroke="#d6b21c" stroke-width="4">
    <rect x="18" y="10" width="76" height="52" rx="4"/>
    <path d="M56 62v18M30 94h52M56 80v14M30 94v-8M82 94v-8"/>
    <circle cx="56" cy="36" r="10"/>
  </svg>
  <h3 class="service-name">MANAGED IT SERVICES</h3>
  <div class="service-rule"></div>
  <p class="service-copy">IT support to take you from where you are to where you would like to be.</p>
</article>

<article class="service" style="left:412px;">
  <svg width="112" height="112" viewBox="0 0 112 112" fill="none" stroke="#d6b21c" stroke-width="4">
    <path d="M56 8 L94 22 V54 C94 78 76 94 56 104 C36 94 18 78 18 54 V22 Z"/>
    <path d="M38 56 L52 70 L76 44"/>
  </svg>
  <h3 class="service-name">SECURITY</h3>
  <div class="service-rule"></div>
  <p class="service-copy">Ensure you are fully secure, able to connect and rotected from the unexpected.</p>
</article>

<article class="service" style="left:808px;">
  <svg width="112" height="112" viewBox="0 0 112 112" fill="none" stroke="#d6b21c" stroke-width="4">
    <path d="M10 30 H44 L52 40 H100 V92 H10 Z"/>
    <path d="M30 40 L60 14 L84 40"/>
  </svg>
  <h3 class="service-name">STORAGE &amp; MANAGEMENT</h3>
  <div class="service-rule"></div>
  <p class="service-copy">Improve the performance, recoverability and maximise your data insights</p>
</article>

<section class="promise" role="img" aria-label="Dark photograph of a man looking at floating technology hexagons">
  <div class="promise-line" style="top:158px;">WE <span class="accent">DELIVER RESULTS &amp;</span></div>
  <div class="promise-line" style="top:218px;">ARE OBSESSED WITH EXCELLENCE</div>
  <div class="promise-button">FIND OUT MORE</div>
</section>

<h2 class="section-title heading" style="top:2640px;">TURBOCHARGE YOUR BUSINESS!</h2>
<div class="title-rule" style="top:2722px;"></div>
<p class="turbo-copy">The Moravel IT Team don't just sit on the sideline closing tickets, we focus on ensuring that our clients TURBOCHARGE their business.</p>

<div class="turbo-art" role="img" aria-label="Illustration of a glowing yellow light bulb above grey bulbs"></div>

<ul class="benefits">
  <li><svg width="24" height="20" viewBox="0 0 24 20"><path d="M2 10 L9 17 L22 3" fill="none" stroke="#d6b21c" stroke-width="4"/></svg>Support Desk</li>
  <li><svg width="24" height="20" viewBox="0 0 24 20"><path d="M2 10 L9 17 L22 3" fill="none" stroke="#d6b21c" stroke-width="4"/></svg>Dedicated Service Delivery Manager</li>
  <li><svg width="24" height="20" viewBox="0 0 24 20"><path d="M2 10 L9 17 L22 3" fill="none" stroke="#d6b21c" stroke-width="4"/></svg>Advanced Security</li>
  <li><svg width="24" height="20" viewBox="0 0 24 20"><path d="M2 10 L9 17 L22 3" fill="none" stroke="#d6b21c" stroke-width="4"/></svg>Server Back ups</li>
  <li><svg width="24" height="20" viewBox="0 0 24 20"><path d="M2 10 L9 17 L22 3" fill="none" stroke="#d6b21c" stroke-width="4"/></svg>Quarterly Reviews</li>
</ul>

<footer class="footer">© Copyright 2020 Moravel.All Rights Reserved</footer>

</body>
</html>
```